Partnership Enterprise Architects looking for Business Flyer (Dutch laguage)

We are a partnership of independent IT Architects working in various roles within our clients (Goverment agencies, Financial institutions and for profit companies). With this flyer we would like to promote ourselves in a inviting but still business like way. We would like to see our logo and name (Maatschap Veltrix) and the graphs and text we used in our example as the basis of the flyer. Anything else is up to your creativity. Colors and 'look and feel' of the graphs may be altered as long as the text (Dutch language remains unchanged). We think a 2 page A4 format flyer would serve best, but are open to suggestions.

Target Market(s)

Clients in the field of Government agencies, Financial institutions and for profit comapnies as well as possible future partners in the ICT Architect field

Industry/Entity Type

Business

Font styles to use
Sans Serif
Other font styles liked:
• Calibri 11 is our standard font

Colors

Designer to choose colors to be used in the design.

Requirements
Must have
• The text (verbatim in the Dutch laguage) as well as the graphs (they may be altered as you see fit as long as the general point and meaning remain the same). Logo preferably upper right corner. 2 A4 double sided flyer in one piece (

```html
<!DOCTYPE html>
<html lang="nl">
<head>
<meta charset="utf-8">
<title>Maatschap Veltrix – flyer</title>
<link href="https://fonts.googleapis.com/css2?family=Carlito:wght@400;700&family=Fira+Sans+Condensed:wght@400;500&display=swap" rel="stylesheet">
<style>
:root{
  --gold:#c8a12b;
  --gold-light:#e8d08a;
  --grey:#7b7b7b;
  --grey-dark:#5e5e5e;
  --grey-light:#d9d9d9;
  --ink:#4a4a4a;
  --page:#ffffff;
  --backdrop:#a8a8a8;
  --plan:#8a5aa8;
  --build:#e9c532;
  --enable:#6db04a;
  --manage:#4a86c8;
}
*{margin:0;padding:0;box-sizing:border-box}
html,body{width:837px;height:1200px;overflow:hidden}
body{background:var(--backdrop);font-family:"Carlito",sans-serif;color:var(--ink);position:relative}
.spread{position:absolute;left:63px;width:705px;height:499px;background:var(--page);overflow:hidden}
.spread--outside{top:81px}
.spread--inside{top:638px}
.page{position:absolute;top:0;width:352px;height:499px;overflow:hidden}
.page--left{left:0}
.page--right{left:353px}
.abs{position:absolute}
.heading{font-family:"Fira Sans Condensed",sans-serif;font-weight:500}

/* outside left */
.hero-illustration{left:0;top:0;width:353px;height:103px;background:linear-gradient(135deg,#e9e9e7,#cfcfcc 70%,#b9b9b7)}
.process-panel{left:0;top:103px;width:353px;height:201px;background:var(--grey)}
.process-panel__title{left:24px;top:18px;width:300px;font-size:8.4px;line-height:12px;color:#fff}
.process-panel__rule{left:24px;top:45px;width:275px;height:1px;background:var(--gold)}
.process-diagram{left:0;top:0}
.contact{left:24px;top:314px}
.contact__title{font-size:14px;color:var(--grey-dark);letter-spacing:.3px}
.contact__rule{width:98px;height:1px;background:var(--gold);margin-top:3px}
.contact__block{font-size:8.4px;line-height:12px;margin-top:12px;color:var(--ink)}
.brand{font-family:"Fira Sans Condensed",sans-serif;font-weight:500;color:#2f2f2f;line-height:.92;display:flex;align-items:flex-start;gap:5px}
.brand__mark{width:10px;height:10px;background:var(--gold);border-radius:50%;margin-top:3px}
.brand--contact{left:240px;top:388px;font-size:22px}
.site-band{left:0;top:467px;width:353px;height:32px;background:var(--gold);color:#fff;font-size:15px;text-align:center;line-height:32px}

/* outside right */
.cover-photo{left:0;top:0;width:352px;height:499px;background:linear-gradient(160deg,#f0e9e2 0%,#e3c9b5 30%,#c4a08c 50%,#7d8ea3 75%,#3e5470 100%)}
.cover-shapes{left:0;top:0}
.brand--cover{left:14px;top:222px;font-size:30px}
.cover-title{left:18px;top:318px;font-size:17px;color:#fff}
.cover-text{left:18px;top:344px;width:164px;font-size:6.6px;line-height:9.6px;color:#fff;font-weight:700}

/* inside top band */
.work-photo{left:353px;top:0;width:352px;height:168px;background:linear-gradient(120deg,#cfcac3 0%,#9e9a94 40%,#5b5855 75%,#3a3836 100%)}
.work-title{left:24px;top:14px;font-size:18px;color:#fff}
.work-text{left:24px;top:46px;width:322px;font-size:7.3px;line-height:11px;color:#fff;text-align:justify}
.work-text p+p{margin-top:7px}

/* inside lower */
.section-title{font-size:17px;color:var(--grey-dark)}
.section-rule{height:1px;background:var(--gold);margin-top:2px}
.offer{left:24px;top:184px;width:320px}
.offer__intro{font-size:8.4px;margin-top:7px}
.ticklist{list-style:none;margin-top:5px}
.ticklist li{font-size:8.8px;line-height:13.4px;display:flex;align-items:center;gap:7px}
.tick{width:7px;height:7px;flex:none}
.offer__after{font-size:8.4px;margin-top:3px}

.matrix{left:24px;top:356px;width:318px;height:132px;display:grid;grid-template-columns:20px 1fr 1fr 1fr;grid-template-rows:44px 44px 44px;gap:1px;background:#fff}
.matrix__label{background:var(--gold);color:#fff;font-size:5px;display:flex;align-items:center;justify-content:center}
.matrix__label span{transform:rotate(-90deg);white-space:nowrap}
.matrix__cell{font-size:4.8px;line-height:6px;padding:3px 0 0 8px}
.matrix__cell--light{background:var(--grey-light);color:#444}
.matrix__cell--dark{background:var(--grey);color:#fff}
.matrix__tools{grid-column:2 / 5;display:grid;grid-template-columns:repeat(4,1fr);background:#fff}
.matrix__tools div{font-size:4.6px;line-height:5.8px;padding:0 0 0 4px;color:#444}
.matrix__tools b{display:block;background:var(--gold);color:#fff;font-weight:700;padding:1px 0 1px 4px;margin:0 0 2px -4px}

.experience{left:374px;top:184px;width:320px}
.experience p{font-size:8.4px;line-height:11px;margin-top:10px}
.experience .ticklist{display:grid;grid-template-columns:142px 1fr;margin-top:8px}

.profile{left:374px;top:361px;width:100px}
.profile__title{font-size:8.4px;line-height:12px}
.profile__rule{height:1px;background:var(--gold);margin-top:2px}
.legend{margin-top:8px;font-size:4.8px;line-height:6px}
.legend div{display:flex;gap:4px;align-items:flex-start;margin-top:5px}
.dot{width:7px;height:7px;border-radius:50%;flex:none}
.dot--avg{background:var(--build)}
.dot--high{background:var(--enable)}

.ecf{left:480px;top:348px;width:210px;font-size:3.8px;line-height:6.5px}
.ecf__head{margin-left:130px;width:80px;background:var(--grey-light);text-align:center;color:#333}
.ecf__row{display:grid;grid-template-columns:18px 112px repeat(5,16px);height:6.5px;border-bottom:.5px solid #fff}
.ecf__row span{padding-left:2px;white-space:nowrap;overflow:hidden}
.ecf__row i{display:flex;align-items:center;justify-content:center;font-style:normal}
.ecf__row i.y::after,.ecf__row i.g::after{content:"";width:5px;height:5px;border-radius:50%}
.ecf__row i.y::after{background:var(--build)}
.ecf__row i.g::after{background:var(--enable)}
.ecf__row--plan{background:var(--plan);color:#fff}
.ecf__row--plan-item{background:#dccbe6}
.ecf__row--build{background:var(--build);color:#333}
.ecf__row--build-item{background:#f6eaba}
.ecf__row--enable{background:var(--enable);color:#fff}
.ecf__row--enable-item{background:#d3e9c6}
.ecf__row--manage{background:var(--manage);color:#fff}
.ecf__row--manage-item{background:#cddff1}
.fold{left:352px;top:168px;width:1px;height:331px;background:rgba(0,0,0,.08)}
</style>
</head>
<body>

<!-- OUTSIDE SPREAD -->
<section class="spread spread--outside">
  <div class="page page--left">
    <div class="abs hero-illustration" role="img" aria-label="Zakenman met gekruiste armen voor een krijtbord met schetsen van grafieken, cloud en teamwerk"></div>

    <div class="abs process-panel">
      <p class="abs process-panel__title">Core competenties van Veltrix gepositioneerd op het<br>ICT Business Process (e-CF Dimension 1)</p>
      <div class="abs process-panel__rule"></div>
      <svg class="abs process-diagram" width="353" height="201" viewBox="0 0 353 201" font-family="Carlito, sans-serif">
        <!-- manage band -->
        <polygon points="24,64 224,64 236,75 224,86 24,86" fill="#d9d9d9"/>
        <polygon points="24,64 118,64 118,86 24,86" fill="#cfcfcf"/>
        <text x="50" y="84" font-size="4.6" fill="#fff">Business Management</text>
        <text x="126" y="84" font-size="4.6" fill="#fff">Technical Management</text>
        <text x="205" y="69" font-size="5" fill="#fff">Manage</text>
        <!-- process chevrons -->
        <polygon points="24,92 84,92 102,122 84,151 24,151 24,92" fill="#e3e3e3"/>
        <polygon points="90,92 150,92 168,122 150,151 90,151 108,122" fill="#c9c9c9"/>
        <polygon points="156,92 218,92 236,122 218,151 156,151 174,122" fill="#dedede"/>
        <text x="62" y="127" font-size="6" fill="#555">Design</text>
        <text x="66" y="148" font-size="5" fill="#555">PLAN</text>
        <text x="124" y="119" font-size="5" fill="#fff">Develop</text>
        <text x="128" y="125" font-size="5" fill="#fff">ment</text>
        <text x="124" y="148" font-size="5" fill="#fff">BUILD</text>
        <text x="188" y="120" font-size="5.6" fill="#666">Service &amp;</text>
        <text x="188" y="128" font-size="5.6" fill="#666">operation</text>
        <text x="198" y="148" font-size="5" fill="#666">RUN</text>
        <!-- support band -->
        <polygon points="24,157 224,157 236,169 224,182 24,182" fill="#e6e6e6"/>
        <text x="45" y="175" font-size="4.8" fill="#fff">Support</text>
        <text x="206" y="178" font-size="5" fill="#fff">Enable</text>
        <!-- role circles -->
        <g fill="#c8a12b" stroke="#e8d08a" stroke-width="1">
          <circle cx="130" cy="60" r="13"/>
          <circle cx="168" cy="60" r="13"/>
          <circle cx="40" cy="104" r="13"/>
          <circle cx="36" cy="143" r="13"/>
          <circle cx="100" cy="143" r="13"/>
        </g>
        <g font-size="4.2" fill="#fff" text-anchor="middle">
          <text x="130" y="57">Quality</text><text x="130" y="62">assurance</text><text x="130" y="67">manager</text>
          <text x="168" y="53">Chief</text><text x="168" y="58">information</text><text x="168" y="63">security</text><text x="168" y="68">officer</text>
          <text x="40" y="103">Business</text><text x="40" y="108">analyst</text>
          <text x="36" y="142">Enterprise</text><text x="36" y="147">architect</text>
          <text x="100" y="142">Systems</text><text x="100" y="147">architect</text>
        </g>
        <!-- statement ovals -->
        <ellipse cx="298" cy="86" rx="38" ry="12" fill="#c8a12b" stroke="#e8d08a"/>
        <ellipse cx="298" cy="147" rx="38" ry="12" fill="#c8a12b" stroke="#e8d08a"/>
        <g font-size="4.6" fill="#fff" text-anchor="middle">
          <text x="298" y="85">We helpen de</text><text x="298" y="91">beslisser beslissen</text>
          <text x="298" y="146">De klantvraag staat</text><text x="298" y="152">centraal ALTIJD</text>
        </g>
      </svg>
    </div>

    <div class="abs contact">
      <h2 class="contact__title heading">CONTACT</h2>
      <div class="contact__rule"></div>
      <p class="contact__block">Lindelaan 14<br>2712 AB Zoetermeer</p>
      <p class="contact__block">Werkhuis Utrecht Centrum<br>Kanaalweg 41<br>3526 KL Utrecht</p>
      <p class="contact__block">T. 079 000 1234<br>E. contact@nordvale-groep.nl<br>KvK: 12345678</p>
    </div>
    <div class="abs brand brand--contact"><span>NORDVALE<br>GROEP</span><span class="brand__mark"></span></div>
    <div class="abs site-band">www.nordvale-groep.nl</div>
  </div>

  <div class="page page--right">
    <div class="abs cover-photo" role="img" aria-label="Zakenman met tablet in dubbele belichting met een skyline bij zonsondergang"></div>
    <svg class="abs cover-shapes" width="352" height="499" viewBox="0 0 352 499">
      <polygon points="0,0 36,0 268,372 176,499 0,499" fill="#ffffff"/>
      <polygon points="0,310 196,310 232,372 176,499 0,499" fill="#c8a12b"/>
      <polygon points="176,499 352,499 352,390" fill="#6f6f6f"/>
    </svg>
    <div class="abs brand brand--cover"><span>NORDVALE<br>GROEP</span><span class="brand__mark"></span></div>
    <h1 class="abs cover-title heading">Maatschap Veltrix</h1>
    <p class="abs cover-text">De maten vormen een collectief van initiatiefrijke, ervaren (15 jaar of meer) en gedreven zelfstandige ondernemers. We vinden dat de bedrijfsvraagstukken leidend zijn. IT-producten en -pakketten, architectuur, methoden en technieken zijn hulpmiddelen en geen doelen op zich. Het ondersteunen van de opdrachtgever bij het demand-vraagstuk en het stellen van de goede vraag aan de IT-leverende partij, staat bij ons centraal. We zijn zelfstandig ondernemers zonder binding aan een product of methode. We zijn een verrijking, geen beperking van uw organisatie en we voeren uw agenda uit.</p>
  </div>
</section>

<!-- INSIDE SPREAD -->
<section class="spread spread--inside">
  <div class="abs work-photo" role="img" aria-label="Zakelijke werkplek met laptop en een wereldnetwerk van verbonden punten"></div>
  <svg class="abs" style="left:0;top:0" width="705" height="168" viewBox="0 0 705 168">
    <polygon points="0,0 353,0 432,84 353,168 0,168" fill="#c8a12b"/>
  </svg>
  <h2 class="abs work-title heading">Hoe we WERKEN</h2>
  <div class="abs work-text">
    <p>We helpen de beslisser beslissen. Dit doen we door de business eisen en wensen helder te maken en die te vertalen in (business en IT) oplossingen. Het vormen van oplossingen doen we door het toepassen van, door de jaren heen, bij andere klanten opgebouwde best practices.</p>
    <p>Elk van onze ondernemers wordt ondersteund door een omvangrijk kennisnetwerk. We wisselen ervaringen uit en bouwen actief aan onze vakkennis. Op die manier garanderen we dat onze kennis up-to-date is en relevant blijft. De maatschap levert een onder de door de Belastingdienst goedgekeurde modelovereenkomst.</p>
  </div>

  <div class="abs offer">
    <h2 class="section-title heading">Wat we BIEDEN</h2>
    <div class="section-rule" style="width:142px"></div>
    <p class="offer__intro">Een greep uit de bedrijfs- en IT-vraagstukken waarbij we helpen:</p>
    <ul class="ticklist">
      <li><svg class="tick" viewBox="0 0 8 8"><circle cx="4" cy="4" r="3.4" fill="none" stroke="#c8a12b"/><path d="M2.3 4.1l1.2 1.2 2.3-2.5" fill="none" stroke="#c8a12b"/></svg>IT strategie</li>
      <li><svg class="tick" viewBox="0 0 8 8"><circle cx="4" cy="4" r="3.4" fill="none" stroke="#c8a12b"/><path d="M2.3 4.1l1.2 1.2 2.3-2.5" fill="none" stroke="#c8a12b"/></svg>Procesinrichting en -harmonisatie</li>
      <li><svg class="tick" viewBox="0 0 8 8"><circle cx="4" cy="4" r="3.4" fill="none" stroke="#c8a12b"/><path d="M2.3 4.1l1.2 1.2 2.3-2.5" fill="none" stroke="#c8a12b"/></svg>Portfolio management</li>
      <li><svg class="tick" viewBox="0 0 8 8"><circle cx="4" cy="4" r="3.4" fill="none" stroke="#c8a12b"/><path d="M2.3 4.1l1.2 1.2 2.3-2.5" fill="none" stroke="#c8a12b"/></svg>Inrichten van governance</li>
      <li><svg class="tick" viewBox="0 0 8 8"><circle cx="4" cy="4" r="3.4" fill="none" stroke="#c8a12b"/><path d="M2.3 4.1l1.2 1.2 2.3-2.5" fill="none" stroke="#c8a12b"/></svg>Business - IT alignment, IT transformatie</li>
      <li><svg class="tick" viewBox="0 0 8 8"><circle cx="4" cy="4" r="3.4" fill="none" stroke="#c8a12b"/><path d="M2.3 4.1l1.2 1.2 2.3-2.5" fill="none" stroke="#c8a12b"/></svg>Innovatie en vernieuwing</li>
      <li><svg class="tick" viewBox="0 0 8 8"><circle cx="4" cy="4" r="3.4" fill="none" stroke="#c8a12b"/><path d="M2.3 4.1l1.2 1.2 2.3-2.5" fill="none" stroke="#c8a12b"/></svg>Scenario analyse</li>
    </ul>
    <p class="offer__after">Daarnaast bieden we architectuurtraining, -opleiding en -coaching.</p>
  </div>

  <div class="abs matrix">
    <div class="matrix__label"><span>vraagstukken</span></div>
    <div class="matrix__cell matrix__cell--light">IT strategie<br>Business - IT alignment<br>IT transformatie<br>Innovatie en vernieuwing<br>Decentralisatie</div>
    <div class="matrix__cell matrix__cell--dark">Portfolio management<br>Inrichten van governance<br>Business - IT alignment<br>IT transformatie<br>Aanbesteding</div>
    <div class="matrix__cell matrix__cell--light">Procesinrichting<br>Procesharmonisatie<br>Scenario analyse<br>Audit</div>
    <div class="matrix__label"><span>rollen</span></div>
    <div class="matrix__cell matrix__cell--light" style="padding-top:10px">Enterprise architect<br>Business architect<br>Program manager</div>
    <div class="matrix__cell matrix__cell--dark" style="padding-top:10px">Business architect<br>Informatie architect<br>Data architect<br>Delivery manager</div>
    <div class="matrix__cell matrix__cell--light" style="padding-top:6px">Project architect<br>Information architect<br>Solution architect<br>Data architect<br>SOA architect Product owner</div>
    <div class="matrix__label"><span>werkgebieden</span></div>
    <div class="matrix__tools">
      <div><b>Methoden</b>IAF<br>DYA<br>TOGAF<br>GEA<br>BPM<br>UML, modellering</div>
      <div><b>Toolbox</b>Modelleertool<br>Repository<br>Open modeller<br>Procesmodellering</div>
      <div><b>Ontwikkeling</b>SAFe, LESS<br>SCRUM<br>Lean Six Sigma<br>BPR, BPI<br>PRINCE 2<br>MSP</div>
      <div><b>Governance Frameworks</b>ASL, BiSL, ITIL<br>BASEL<br>GDPR<br>Privacy by Design<br>Security by Design</div>
    </div>
  </div>

  <div class="abs experience">
    <h2 class="section-title heading">ERVARING</h2>
    <div class="section-rule" style="width:156px"></div>
    <p>De maten hebben werkervaring in overheid, zorg, onderwijs, transport, telecom, media, financiële dienstverlening, verzekeringen en nutsbedrijven.</p>
    <p>De maten zijn gecertificeerd voor gangbare methoden en industrie standaarden:</p>
    <ul class="ticklist">
      <li><svg class="tick" viewBox="0 0 8 8"><circle cx="4" cy="4" r="3.4" fill="none" stroke="#c8a12b"/><path d="M2.3 4.1l1.2 1.2 2.3-2.5" fill="none" stroke="#c8a12b"/></svg>BPM en Lean Six Sigma</li>
      <li><svg class="tick" viewBox="0 0 8 8"><circle cx="4" cy="4" r="3.4" fill="none" stroke="#c8a12b"/><path d="M2.3 4.1l1.2 1.2 2.3-2.5" fill="none" stroke="#c8a12b"/></svg>SCRUM en SAFe</li>
      <li><svg class="tick" viewBox="0 0 8 8"><circle cx="4" cy="4" r="3.4" fill="none" stroke="#c8a12b"/><path d="M2.3 4.1l1.2 1.2 2.3-2.5" fill="none" stroke="#c8a12b"/></svg>IAF, DYA, TOGAF en GEA</li>
      <li><svg class="tick" viewBox="0 0 8 8"><circle cx="4" cy="4" r="3.4" fill="none" stroke="#c8a12b"/><path d="M2.3 4.1l1.2 1.2 2.3-2.5" fill="none" stroke="#c8a12b"/></svg>BISL/ASL/ITIL</li>
      <li><svg class="tick" viewBox="0 0 8 8"><circle cx="4" cy="4" r="3.4" fill="none" stroke="#c8a12b"/><path d="M2.3 4.1l1.2 1.2 2.3-2.5" fill="none" stroke="#c8a12b"/></svg>Archimate</li>
      <li><svg class="tick" viewBox="0 0 8 8"><circle cx="4" cy="4" r="3.4" fill="none" stroke="#c8a12b"/><path d="M2.3 4.1l1.2 1.2 2.3-2.5" fill="none" stroke="#c8a12b"/></svg>IREB</li>
    </ul>
  </div>

  <div class="abs profile">
    <p class="profile__title">The Veltrix Group<br>e-CF Groupsprofile<br>CORE competences</p>
    <div class="profile__rule"></div>
    <div class="legend">
      <div><span class="dot dot--avg"></span>average competence level</div>
      <div><span class="dot dot--high"></span>highest competence level in the group</div>
    </div>
  </div>

  <div class="abs ecf">
    <div class="ecf__head">e-CF levels</div>
    <div class="ecf__row ecf__row--plan"><span>A</span><span>PLAN</span><i>e-1</i><i>e-2</i><i>e-3</i><i>e-4</i><i>e-5</i></div>
    <div class="ecf__row ecf__row--plan-item"><span>A.1</span><span>IS and Business Strategy Alignment</span><i></i><i></i><i class="y"></i><i></i><i class="g"></i></div>
    <div class="ecf__row ecf__row--plan-item"><span>A.5</span><span>Architecture Design</span><i></i><i></i><i class="y"></i><i></i><i class="g"></i></div>
    <div class="ecf__row ecf__row--plan-item"><span>A.7</span><span>Technology Trend Monitoring</span><i></i><i></i><i></i><i class="y"></i><i class="g"></i></div>
    <div class="ecf__row ecf__row--plan-item"><span>A.9</span><span>Innovating</span><i></i><i></i><i class="y"></i><i class="g"></i><i></i></div>
    <div class="ecf__row ecf__row--build"><span>B</span><span>BUILD</span><i>e-1</i><i>e-2</i><i>e-3</i><i>e-4</i><i>e-5</i></div>
    <div class="ecf__row ecf__row--build-item"><span>B.2</span><span>Component Integration</span><i></i><i></i><i class="y"></i><i class="g"></i><i></i></div>
    <div class="ecf__row ecf__row--build-item"><span>B.6</span><span>Systems Engineering</span><i></i><i></i><i class="y"></i><i class="g"></i><i></i></div>
    <div class="ecf__row ecf__row--enable"><span>D</span><span>ENABLE</span><i>e-1</i><i>e-2</i><i>e-3</i><i>e-4</i><i>e-5</i></div>
    <div class="ecf__row ecf__row--enable-item"><span>D.1</span><span>Information Security Strategy Development</span><i></i><i></i><i class="y"></i><i class="g"></i><i></i></div>
    <div class="ecf__row ecf__row--enable-item"><span>D.2</span><span>ICT Quality Strategy Development</span><i></i><i></i><i class="y"></i><i class="g"></i><i></i></div>
    <div class="ecf__row ecf__row--enable-item"><span>D.10</span><span>Information and Knowledge Management</span><i></i><i></i><i></i><i class="y"></i><i class="g"></i></div>
    <div class="ecf__row ecf__row--enable-item"><span>D.11</span><span>Needs Identification</span><i></i><i></i><i></i><i class="y"></i><i class="g"></i></div>
    <div class="ecf__row ecf__row--manage"><span>E</span><span>MANAGE</span><i>e-1</i><i>e-2</i><i>e-3</i><i>e-4</i><i>e-5</i></div>
    <div class="ecf__row ecf__row--manage-item"><span>E.2</span><span>Project and Portfolio Management</span><i></i><i></i><i class="y"></i><i class="g"></i><i></i></div>
    <div class="ecf__row ecf__row--manage-item"><span>E.6</span><span>ICT Quality Management</span><i></i><i></i><i class="y"></i><i class="g"></i><i></i></div>
    <div class="ecf__row ecf__row--manage-item"><span>E.7</span><span>Business Change Management</span><i></i><i></i><i class="y"></i><i class="g"></i><i></i></div>
    <div class="ecf__row ecf__row--manage-item"><span>E.9</span><span>IS Governance</span><i></i><i></i><i class="y"></i><i></i><i></i></div>
  </div>
  <div class="abs fold"></div>
</section>

</body>
</html>
```